IT services provider needs a go to market lifecycle design

We need our go to market lifecycle diagram to be developed to show the flow of our propositions. We believe that customers could engage us at any stage of the cycle and that it would lead on to the next proposition, or, they could join at the start (Assess and Advice) and we would provide them with our services throughout the cycle.

```html
<!DOCTYPE html>
<html lang="en">
<head>
<meta charset="utf-8">
<title>Go-to-Market Lifecycle</title>
<link rel="stylesheet" href="https://fonts.googleapis.com/css2?family=Archivo+Black&family=Oswald:wght@700&display=swap">
<style>
  :root {
    --bg: #ffffff;
    --assess: #5b8ee8;
    --assess-edge: #3f6fc4;
    --architect: #4fcd2f;
    --architect-edge: #35a51c;
    --manage: #f1ab12;
    --manage-edge: #cf8a05;
    --recycle: #ea3d5c;
    --recycle-edge: #c4233f;
    --label: #ffffff;
    --core: #e3262b;
    --core-shade: #9e1216;
  }
  html, body {
    margin: 0;
    padding: 0;
    width: 1200px;
    height: 1200px;
    overflow: hidden;
    background: var(--bg);
  }
  .lifecycle {
    display: block;
    width: 1200px;
    height: 1200px;
  }
  .stage-assess { fill: var(--assess); stroke: var(--assess-edge); }
  .stage-architect { fill: var(--architect); stroke: var(--architect-edge); }
  .stage-manage { fill: var(--manage); stroke: var(--manage-edge); }
  .stage-recycle { fill: var(--recycle); stroke: var(--recycle-edge); }
  .stage-shape { stroke-width: 3; stroke-linejoin: round; }
  .stage-label {
    font-family: "Archivo Black", "Arial Black", sans-serif;
    fill: var(--label);
    text-anchor: middle;
    letter-spacing: 3px;
  }
  .core-title {
    font-family: "Oswald", "Impact", sans-serif;
    font-weight: 700;
    fill: var(--core);
    text-anchor: middle;
    paint-order: stroke;
    stroke: var(--core-shade);
    stroke-width: 2px;
  }
</style>
</head>
<body>
<svg class="lifecycle" viewBox="0 0 1200 1200" role="img" aria-label="Go-to-market lifecycle: Assess and Advise, Architect and Transform, Manage and Operate, Recycle and Retire, around the Datacentre Workspace">
  <defs>
    <path id="arc-top-outer" d="M331.3 331.3 A380 380 0 0 1 868.7 331.3"/>
    <path id="arc-top-inner" d="M377.3 377.3 A315 315 0 0 1 822.7 377.3"/>
    <path id="arc-bottom-inner" d="M363.1 836.9 A335 335 0 0 0 836.9 836.9"/>
    <path id="arc-bottom-outer" d="M310.1 889.9 A410 410 0 0 0 889.9 889.9"/>
    <path id="stage-arrow" d="M150.1 592.1 A450 450 0 0 1 592.1 150.1 L643.5 245.7 L595.4 335 A265 265 0 0 0 335 595.4 L246.5 550.3 Z"/>
  </defs>

  <g class="cycle-ring" transform="rotate(3 600 600)">
    <use href="#stage-arrow" class="stage-shape stage-assess"/>
    <use href="#stage-arrow" class="stage-shape stage-architect" transform="rotate(90 600 600)"/>
    <use href="#stage-arrow" class="stage-shape stage-manage" transform="rotate(180 600 600)"/>
    <use href="#stage-arrow" class="stage-shape stage-recycle" transform="rotate(270 600 600)"/>
  </g>

  <g class="stage-text-assess" transform="rotate(-42 600 600)">
    <text class="stage-label" font-size="66" letter-spacing="8"><textPath href="#arc-top-outer" startOffset="50%">ASSESS</textPath></text>
    <text class="stage-label" font-size="42"><textPath href="#arc-top-inner" startOffset="50%">&amp; ADVISE</textPath></text>
  </g>

  <g class="stage-text-architect" transform="rotate(48 600 600)">
    <text class="stage-label" font-size="60"><textPath href="#arc-top-outer" startOffset="50%">ARCHITECT</textPath></text>
    <text class="stage-label" font-size="38"><textPath href="#arc-top-inner" startOffset="50%">&amp; TRANSFORM</textPath></text>
  </g>

  <g class="stage-text-manage" transform="rotate(-42 600 600)">
    <text class="stage-label" font-size="50"><textPath href="#arc-bottom-inner" startOffset="50%">MANAGE</textPath></text>
    <text class="stage-label" font-size="62"><textPath href="#arc-bottom-outer" startOffset="50%">&amp; OPERATE</textPath></text>
  </g>

  <g class="stage-text-recycle" transform="rotate(48 600 600)">
    <text class="stage-label" font-size="54"><textPath href="#arc-bottom-inner" startOffset="50%">RECYCLE</textPath></text>
    <text class="stage-label" font-size="68"><textPath href="#arc-bottom-outer" startOffset="50%">&amp; RETIRE</textPath></text>
  </g>

  <g class="cycle-core">
    <text class="core-title" x="600" y="592" font-size="88" textLength="458" lengthAdjust="spacingAndGlyphs">DATACENTRE</text>
    <text class="core-title" x="600" y="690" font-size="88" textLength="430" lengthAdjust="spacingAndGlyphs">WORKSPACE</text>
  </g>
</svg>
</body>
</html>
```